Pediatric Occupational Therapy Brochure Design

This design really needs to stand out, especially with all the wordage that I have included. These brochures will be given to doctors, future clients, and caregivers. I have included the logo on by brochure, so incorporating the same or similar colors would be fantastic. A trifold brochure would probably be best to fit all the information, as this is a new business and needs to convey all the information in a way that people will read.

Target Market(s)

Doctor's offices and caregivers of children with disabilities.

Industry/Entity Type

Health Care

Font styles to use
Serif
Sans Serif

Colors
33a6d7
85acd3
ffffff
33b8a4
86cfc7

Requirements
Must have
• I would like the same colors of the logo incorporated in the brochure design.
Nice to have
• I would like to see the butterfly somehow in the background or used in the design. Also a trifold or two page design would be greatly appreciated as long as the information can fit.

```html
<!DOCTYPE html>
<html lang="en">
<head>
<meta charset="utf-8">
<title>Willow Therapy – Trifold Brochure</title>
<link rel="stylesheet" href="https://fonts.googleapis.com/css2?family=Days+One&family=Lato:wght@400;700;900&family=Playfair+Display:wght@400&display=swap">
<style>
  :root {
    --blue: #33a6d7;
    --blue-deep: #17688f;
    --teal: #33b8a4;
    --teal-soft: #86cfc7;
    --sky: #85acd3;
    --white: #ffffff;
    --charcoal: #3f4347;
    --ink: #2b2b2b;
    --grey-text: #5d6266;
    --paper: #f1f1f1;
    --paper-shade: #d9d9d9;
  }
  * { box-sizing: border-box; margin: 0; padding: 0; }
  html, body { width: 1200px; height: 855px; overflow: hidden; background: var(--white); }
  .brochure { position: relative; width: 1200px; height: 855px; display: flex; font-family: "Lato", sans-serif; color: var(--ink); }
  .panel { position: relative; height: 855px; overflow: hidden; }

  /* Left panel */
  .panel-services { width: 408px; }
  .panel-services .backdrop { position: absolute; inset: 0; }
  .services-title { position: absolute; left: 52px; top: 314px; font-family: "Days One", sans-serif; font-size: 23px; line-height: 30px; color: var(--white); letter-spacing: .3px; }
  .services-list { position: absolute; left: 58px; top: 378px; list-style: none; }
  .services-list li { position: relative; padding-left: 20px; font-weight: 700; font-size: 19px; line-height: 25.2px; color: #22262b; }
  .services-list li::before { content: ""; position: absolute; left: 0; top: 8px; width: 9px; height: 9px; border-radius: 50%; background: var(--teal-soft); border: 1.5px solid var(--white); }

  /* Middle panel */
  .panel-info { width: 397px; background: linear-gradient(90deg, var(--paper-shade) 0%, var(--paper) 8%, var(--white) 50%, var(--paper) 92%, var(--paper-shade) 100%); text-align: center; }
  .info-heading { font-family: "Days One", sans-serif; color: var(--teal); font-size: 18px; line-height: 26px; letter-spacing: .4px; }
  .get-started { position: absolute; left: 25px; right: 25px; top: 84px; }
  .get-started p { margin-top: 8px; font-size: 20px; line-height: 27px; color: var(--ink); text-align: justify; text-align-last: center; }
  .schedule { position: absolute; left: 0; right: 0; top: 316px; }
  .schedule .call { font-family: "Days One", sans-serif; font-size: 19px; color: var(--charcoal); margin-top: 2px; }
  .hours { position: absolute; left: 0; right: 0; top: 448px; }
  .hours .strong { font-weight: 900; font-size: 19.5px; line-height: 26px; color: #1f1f1f; }
  .contact { position: absolute; left: 0; right: 0; top: 556px; }
  .contact p { font-size: 19px; line-height: 26px; color: var(--ink); }
  .contact .label { font-family: "Days One", sans-serif; color: var(--teal); font-size: 17px; line-height: 26px; }

  /* Right panel */
  .panel-cover { width: 395px; background: linear-gradient(180deg, var(--white) 0%, var(--paper) 100%); }
  .panel-cover .backdrop { position: absolute; inset: 0; }
  .brand { position: absolute; left: 92px; top: 52px; display: flex; align-items: center; gap: 12px; }
  .brand-name { font-family: "Playfair Display", serif; font-size: 34px; color: var(--grey-text); }
  .brand-dot { width: 40px; height: 40px; border-radius: 50%; background: var(--teal-soft); }
  .brand-email { position: absolute; left: 0; right: 0; top: 132px; text-align: center; font-size: 17px; letter-spacing: 2px; color: var(--grey-text); }
</style>
</head>
<body>
<main class="brochure">

  <section class="panel panel-services">
    <svg class="backdrop" width="408" height="855" viewBox="0 0 408 855">
      <defs>
        <linearGradient id="servicesBlue" x1="0" y1="0" x2="1" y2="1">
          <stop offset="0" stop-color="var(--blue-deep)"/>
          <stop offset="1" stop-color="var(--blue)"/>
        </linearGradient>
        <linearGradient id="familyPhotoTone" x1="0" y1="0" x2="1" y2="1">
          <stop offset="0" stop-color="#f3dcc4"/>
          <stop offset=".55" stop-color="#e9c9a6"/>
          <stop offset="1" stop-color="#c9b39c"/>
        </linearGradient>
      </defs>
      <rect width="408" height="855" fill="url(#servicesBlue)"/>
      <path d="M0 0H408V172C300 230 150 295 0 310Z" fill="var(--teal)"/>
      <path d="M0 0H408V162C300 218 150 284 0 298Z" fill="var(--charcoal)"/>
      <path d="M0 0H408V154C300 208 150 274 0 288Z" fill="var(--white)"/>
      <path d="M0 0H408V148C300 200 150 266 0 280Z" fill="url(#familyPhotoTone)" role="img" aria-label="Photo of a smiling mother and daughter holding a colourful pinwheel"/>
      <path d="M0 855V808C150 806 300 795 408 782V855Z" fill="var(--white)"/>
      <path d="M0 855V816C150 814 300 803 408 790V855Z" fill="var(--charcoal)"/>
    </svg>
    <h2 class="services-title">Services Offered<br>for Your Child</h2>
    <ul class="services-list">
      <li>Social Skills</li>
      <li>Oral Motor</li>
      <li>Sensory Activities</li>
      <li>Feeding</li>
      <li>Handling Techniques</li>
      <li>Handwriting</li>
      <li>Home Exercise Program</li>
      <li>Therapeutic Taping</li>
      <li>Auditory Listening<br>Program (ALP)</li>
      <li>Neuro-Developmental<br>Treatment</li>
      <li>Patient/Parent Education</li>
      <li>Postural Reeducation</li>
      <li>Sensory Integration</li>
      <li>Therapeutic play</li>
      <li>and much more</li>
    </ul>
  </section>

  <section class="panel panel-info">
    <div class="get-started">
      <h2 class="info-heading">HOW TO GET STARTED!</h2>
      <p>If you or someone you know has concerns about their child’s development, discuss with your doctor the concern and request a prescription for an occupational therapy evaluation</p>
    </div>
    <div class="schedule">
      <h2 class="info-heading">TO SCHEDULE<br>AN APPOINTMENT</h2>
      <p class="call">CALL (555) 014-2290</p>
    </div>
    <div class="hours">
      <h2 class="info-heading">BUSINESS HOURS</h2>
      <p class="strong">Monday-Saturday</p>
      <p class="strong">8:00am-7:00pm</p>
    </div>
    <address class="contact" style="font-style:normal">
      <h2 class="info-heading">Willow Therapy, LLC</h2>
      <p>48 Maple Ave, Riverton,<br>Texas 78000</p>
      <p class="label">Phone:</p>
      <p>(555) 014-2290</p>
      <p class="label">email:</p>
      <p>hello@willowtherapy.com</p>
    </address>
  </section>

  <section class="panel panel-cover">
    <svg class="backdrop" width="395" height="855" viewBox="0 0 395 855">
      <defs>
        <linearGradient id="clinicPhotoTone" x1="0" y1="0" x2="1" y2="1">
          <stop offset="0" stop-color="#eef0f2"/>
          <stop offset=".6" stop-color="#e6d6c8"/>
          <stop offset="1" stop-color="#d8c2ad"/>
        </linearGradient>
      </defs>
      <circle cx="262" cy="560" r="248" fill="var(--blue)"/>
      <circle cx="272" cy="498" r="248" fill="var(--teal)"/>
      <circle cx="252" cy="530" r="232" fill="var(--white)"/>
      <circle cx="252" cy="530" r="224" fill="none" stroke="var(--charcoal)" stroke-width="7"/>
      <circle cx="252" cy="530" r="214" fill="var(--white)"/>
      <circle cx="252" cy="530" r="208" fill="url(#clinicPhotoTone)" role="img" aria-label="Photo of a therapist with a stethoscope examining a smiling toddler holding a teddy bear"/>
    </svg>
    <div class="brand">
      <span class="brand-name">Willow Therapy</span>
      <span class="brand-dot"></span>
    </div>
    <p class="brand-email">hello@willowtherapy.com</p>
  </section>

</main>
</body>
</html>
```